Yoga Instrucor

I need my personal business cards, i would like the front a kind of light but vibrant red and matt gold.

Industry/Entity Type

Business

Contact Information for Business Card

Cordelia Hastrup
Yoga Instructor
RYT 200, BROKU (NYC) Yoga RYT 500,
CPR/ AED Certified,
hastrupcordelia@quillbox.com
512 604 8893
Adult Yoga, Private Yoga, Group Classes, Restorative, Meditation, Child Yoga.

```html
<!DOCTYPE html>
<html lang="en">
<head>
<meta charset="utf-8">
<title>Cordelia Hastrup – Yoga Instructor Business Card</title>
<link rel="stylesheet" href="https://fonts.googleapis.com/css2?family=Great+Vibes&family=Open+Sans:wght@400;600&family=Didact+Gothic&display=swap">
<style>
  :root {
    --page-bg: #e9e6e1;
    --front-red: #e5323a;
    --front-orange: #f28a1e;
    --front-gold: #ffd23a;
    --sun-core: #fffbe0;
    --band-orange: #f08a2c;
    --band-light: #f6b066;
    --title-gold: #f3c316;
    --white: #ffffff;
    --credit-text: #fbe3c8;
    --sky-blue: #3f8fd6;
    --sky-light: #cfe4f5;
    --sky-white: #f7f9fb;
    --pill-fill: rgba(255,255,255,0.88);
    --pill-border: #9aa3ad;
    --ink: #1b1b1b;
    --rule: #555555;
  }
  * { box-sizing: border-box; margin: 0; padding: 0; }
  html, body {
    width: 1200px; height: 900px; overflow: hidden;
    background: var(--page-bg);
  }
  .canvas {
    position: relative; width: 1200px; height: 900px;
    display: flex; justify-content: center; align-items: center; gap: 80px;
  }
  .card {
    position: relative; width: 360px; height: 630px; overflow: hidden;
    box-shadow: 0 8px 24px rgba(0,0,0,0.18);
  }

  /* Front */
  .card-front { background: var(--front-red); }
  .front-art {
    position: absolute; inset: 0;
    background:
      radial-gradient(circle at 58% 30%, var(--sun-core) 0, var(--front-gold) 12%, var(--front-orange) 32%, rgba(240,110,40,0.6) 52%, transparent 75%),
      linear-gradient(180deg, #f5a63a 0%, #ef6a3a 45%, var(--front-red) 75%, #e8443a 100%);
  }
  .front-text {
    position: absolute; left: 0; right: 0; top: 318px; text-align: center;
    font-family: "Open Sans", sans-serif; color: var(--white);
  }
  .front-name {
    font-family: "Great Vibes", cursive; font-size: 50px; font-weight: 400;
    line-height: 1.1; text-shadow: 0 1px 2px rgba(120,30,20,0.35);
  }
  .front-role {
    font-size: 21px; color: var(--title-gold); font-weight: 600; margin-top: 4px;
  }
  .front-contact { font-size: 19px; line-height: 1.35; margin-top: 8px; }
  .front-band {
    position: absolute; left: 0; right: 0; bottom: 0; height: 118px;
    background: linear-gradient(180deg, var(--band-light) 0%, var(--band-orange) 45%, #ea7a24 100%);
    border-top: 1px solid rgba(255,255,255,0.4);
    display: flex; flex-direction: column; justify-content: center; align-items: center;
    font-family: "Open Sans", sans-serif; color: var(--credit-text);
    font-size: 16px; line-height: 1.45; text-align: center;
  }

  /* Back */
  .card-back { background: var(--sky-white); }
  .back-art {
    position: absolute; inset: 0;
    background:
      radial-gradient(ellipse at 30% 55%, rgba(255,255,255,0.95) 0, rgba(255,255,255,0.6) 30%, transparent 60%),
      linear-gradient(160deg, var(--sky-blue) 0%, var(--sky-light) 35%, var(--sky-white) 70%, #eef1f4 100%);
  }
  .service-list {
    position: absolute; top: 46px; left: 38px; right: 38px;
    list-style: none; display: flex; flex-direction: column; gap: 9px;
  }
  .service-item {
    height: 36px; border: 1.5px solid var(--pill-border); border-radius: 9px;
    background: var(--pill-fill);
    font-family: "Didact Gothic", sans-serif; font-size: 20px; color: var(--ink);
    display: flex; align-items: center; justify-content: center;
  }
  .appointment {
    position: absolute; left: 34px; right: 34px; bottom: 40px;
    font-family: "Open Sans", sans-serif; color: var(--ink);
  }
  .appointment-label { font-size: 15px; font-weight: 600; margin-bottom: 6px; }
  .appointment-lines { display: block; }
</style>
</head>
<body>
<main class="canvas">
  <section class="card card-front">
    <div class="front-art" role="img" aria-label="Warm glowing sun with soft bokeh lights in gold, orange and red"></div>
    <div class="front-text">
      <h1 class="front-name">Cordelia Hastrup</h1>
      <p class="front-role">Yoga Instructor</p>
      <p class="front-contact">Phone : 512 604 8893<br>hastrupcordelia@quillbox.com</p>
    </div>
    <div class="front-band">
      <p>RYT 200, BROKU (NYC) Yoga RYT 500</p>
      <p>CPR/ AED Certified</p>
    </div>
  </section>

  <section class="card card-back">
    <div class="back-art" role="img" aria-label="Bright blue sky with soft white clouds"></div>
    <ul class="service-list">
      <li class="service-item">Adult Yoga</li>
      <li class="service-item">Private Yoga</li>
      <li class="service-item">Group Classes</li>
      <li class="service-item">Restorative</li>
      <li class="service-item">Meditation</li>
      <li class="service-item">Child Yoga</li>
      <li class="service-item"></li>
    </ul>
    <div class="appointment">
      <p class="appointment-label">Appointment</p>
      <svg class="appointment-lines" width="292" height="110" viewBox="0 0 292 110">
        <g stroke="var(--rule)" stroke-width="1">
          <line x1="110" y1="2" x2="292" y2="2"/>
          <line x1="0" y1="36" x2="190" y2="36"/>
          <line x1="206" y1="36" x2="292" y2="36"/>
          <line x1="0" y1="70" x2="200" y2="70"/>
          <line x1="216" y1="70" x2="292" y2="70"/>
          <line x1="0" y1="104" x2="292" y2="104"/>
        </g>
      </svg>
    </div>
  </section>
</main>
</body>
</html>
```